Morvetta Designs - Online Shoe Shop

Morvetta is an online shoes and bags shop. We sell Imported Genuine Leather shoes and bags our market is LSM 8-10. We mainly sell women shoes and bags and we will also be introducing men’s shoes and belts.
I would like a website design and development that is responsive, clean, elegant and easy to use. Where customers can make a purchase online.
Have CATEGORIES in SHOE STYLE (i.e. Heels, Sandals, Pumps, Mules, Boots, Sneaker, Flats, etc) and PRICE RANGE should be in South African Rands currency, COLOUR, SIZE.
For shoe images we should be able to add videos as well.
Header and Footer Menu should have the basic menu list. Header Menu (New Arrivals, Preorder, Women’s Collection, Men’s Collection, Summer 2020 Collection, Winter 2020 Collection, Bags, Accessories, Sale, etc
Auto display when the item is SOLD OUT. Add an option for a user to get notification on when the item is back in stock.
Icons to show when shoes are on sale and Show was and now price.
Users to be able to review and rate the items.
Discount codes for new email subscribers.
Consumers should be able to pay using different options, Credit card, QuidLane, EFT, etc
Add an option for discount coupons at checkout.
After placing and order they should receive an email with order receipt.
Site should have a shipping and tracking option. International shipping such as KRT and BOLTAIR. For local shipping in South Africa please add Quickpath Couriers and Zenobi Couriers.
Backend: Backend should be easy to add more categories, items and changing header banners, adding sale alerts. To get notification when the stock is low and sold out. Get notification when an order is placed online so to prepare packing for shipping.
Can we make sure that the SEO is in place and bare in mind all searchy rules to avoid being penalized.
Target Market(s)
Women from age 25-65
LSM 8-10
Entire South Africa and neighboring countries
Industry/Entity Type
Shoe Store
Coding
Coded - Design and coding required
Number of Pages Required
5+ page
Requirements
Must have
- Responsive
Clean
Modern
Shopping cart
Shipping options integration
Newsletter subscription
Social media icons
Nice to have
- The business colors are Gold and White or Gold and Black

```html
<!DOCTYPE html>
<html lang="en">
<head>
<meta charset="utf-8">
<title>Morvetta – Blue High Heels</title>
<link rel="stylesheet" href="https://fonts.googleapis.com/css2?family=Poppins:wght@400;500;600&family=Playfair+Display:ital,wght@0,600;1,400&display=swap">
<style>
:root{
  --gold:#d3a22b;
  --ink:#1f1f1f;
  --text:#555;
  --muted:#9a9a9a;
  --line:#e4e4e4;
  --soft:#f2f2f2;
  --banner:#e9e9e9;
  --white:#fff;
  --shoe:#4a5566;
}
*{box-sizing:border-box;margin:0;padding:0}
html,body{width:865px;height:1200px;overflow:hidden}
body{font-family:"Poppins",sans-serif;color:var(--text);background:var(--soft);font-size:7px}
.page{width:865px;height:1200px;position:relative;background:var(--soft)}
.site{background:var(--white)}
/* top bar */
.topbar{height:26px;background:var(--ink);color:#ddd;display:flex;align-items:center;padding:0 115px;font-size:6.5px}
.topbar .social{display:flex;gap:6px}
.dot{width:9px;height:9px;border-radius:50%;background:var(--gold);display:inline-block}
.topbar .contact{margin-left:auto;display:flex;gap:14px;margin-right:170px}
/* header */
.header{height:72px;display:flex;align-items:center;padding:0 115px}
.brand{display:flex;align-items:center;gap:6px;font-weight:600;font-size:15px;color:var(--ink)}
.brand .mark{width:18px;height:18px;background:var(--ink);border-radius:50%}
.tagline{margin-left:78px;font-family:"Playfair Display",serif;font-style:italic;font-size:10px;color:var(--ink)}
.tagline em{color:var(--gold)}
.search{margin-left:auto;width:120px;height:20px;border:1px solid var(--line);display:flex;align-items:center;padding:0 7px;font-size:6px;color:var(--muted);justify-content:space-between}
.cart{margin-left:18px;position:relative}
.cart .count{position:absolute;top:-4px;right:-5px;width:9px;height:9px;border-radius:50%;background:var(--gold);color:#fff;font-size:5px;text-align:center;line-height:9px}
/* nav */
.nav{height:30px;border-top:1px solid var(--line);border-bottom:1px solid var(--line);display:flex;align-items:center;gap:20px;padding:0 115px;font-size:6.5px;font-weight:500;color:var(--ink)}
.nav .active{color:var(--gold)}
/* banner */
.banner{height:82px;background:var(--banner);display:flex;align-items:center;padding:0 115px;margin-top:8px}
.banner h1{font-size:8px;font-weight:500;color:var(--ink);letter-spacing:.5px;width:200px}
.banner .photo{width:130px;height:62px;background:linear-gradient(90deg,#b98b62,#2b2b2b 50%,#c9a47a);opacity:.85}
.crumbs{margin-left:auto;font-size:6px;color:var(--muted)}
.crumbs b{color:var(--ink);font-weight:500}
/* product */
.product{display:flex;padding:20px 115px 0;gap:32px}
.gallery{width:360px;height:300px;border:1px solid var(--line);display:flex;align-items:center;justify-content:center}
.gallery .shoe{width:200px;height:150px;background:radial-gradient(ellipse at 50% 55%,var(--shoe),#6d7788 55%,#fff 72%)}
.info{flex:1}
.info h2{font-size:10px;font-weight:500;color:var(--ink);margin-bottom:16px}
.specs{display:grid;grid-template-columns:80px 1fr;row-gap:5px;font-size:6px}
.specs dt{color:var(--ink);font-weight:500}
.specs dd{color:var(--muted)}
.rule{border-top:1px solid var(--line);margin:48px 0 12px}
.opts{display:grid;grid-template-columns:80px 1fr;row-gap:10px;font-size:6px;align-items:center}
.opts span{color:var(--ink);font-weight:500}
.swatches{display:flex;gap:6px}
.swatches i{width:12px;height:12px;display:block}
.sel{width:38px;height:13px;border:1px solid var(--line);font-size:6px;padding:0 4px;line-height:11px;color:var(--text)}
.buttons{display:flex;gap:10px;margin-top:26px}
.btn{background:var(--ink);color:#fff;font-size:6px;font-weight:500;padding:7px 11px}
.summary{padding:10px 115px 0;width:520px;font-size:6px;line-height:1.7;color:var(--muted)}
/* tabs */
.tabs{margin:30px 115px 0;border-bottom:1px solid var(--line);display:flex;gap:48px;font-size:7px;font-weight:500;color:var(--ink);padding-left:18px}
.tabs div{padding-bottom:7px}
.tabs .on{color:var(--gold);border-bottom:2px solid var(--gold)}
.tabtext{padding:14px 115px 24px;font-size:6px;line-height:1.8;color:var(--muted)}
/* footer */
.footer{padding:28px 40px 0}
.footcard{background:var(--white);height:320px;display:grid;grid-template-columns:1fr 1.2fr 1fr;padding:34px 75px 0}
.footcard h3{font-size:9px;font-weight:500;color:var(--ink);margin-bottom:16px}
.links{list-style:none;font-size:6px;line-height:2.1;color:var(--muted)}
.links li::before{content:"› ";color:var(--gold)}
.newsletter{text-align:center;border-left:1px solid var(--line);border-right:1px solid var(--line);padding:0 22px}
.newsletter h3{font-family:"Playfair Display",serif;font-weight:600;font-size:16px;letter-spacing:1.5px}
.newsletter p{font-size:6px;line-height:1.7;color:var(--muted)}
.signup{margin:22px auto 0;width:150px;height:24px;border-radius:12px;background:var(--soft);display:flex;align-items:center;justify-content:space-between;padding:0 3px 0 12px;font-size:6px;color:var(--muted)}
.signup b{width:18px;height:18px;border-radius:50%;background:var(--gold);display:flex;align-items:center;justify-content:center}
.contact{padding-left:30px}
.contact p{font-size:6px;line-height:1.9;color:var(--muted)}
.bottombar{margin:0 40px;height:32px;display:flex;align-items:center;padding:0 20px;font-size:6px;color:var(--text);border-top:1px solid var(--line);background:var(--soft)}
.pay{display:flex;gap:6px;align-items:center}
.pay .chip{width:12px;height:8px;background:#c7c7c7;display:inline-block}
.pay strong{font-weight:500;color:var(--ink)}
.powered{margin:0 auto}
.powered b{color:var(--ink);font-weight:600}
.findus{display:flex;gap:5px;align-items:center}
</style>
</head>
<body>
<div class="page">
  <div class="site">
    <div class="topbar">
      <div class="social"><span class="dot"></span><span class="dot"></span><span class="dot"></span></div>
      <div class="contact"><span>TOLL FREE: 080 555 01 234</span><span>hello@morvetta.shop</span></div>
    </div>
    <header class="header">
      <div class="brand"><span class="mark"></span>Morvetta</div>
      <p class="tagline">Discount codes for <em>new email</em> subscribers</p>
      <div class="search">SEARCH <svg width="8" height="8" viewBox="0 0 10 10"><circle cx="4" cy="4" r="3" fill="none" stroke="#999" stroke-width="1.2"/><line x1="6.3" y1="6.3" x2="9" y2="9" stroke="#999" stroke-width="1.2"/></svg></div>
      <div class="cart"><svg width="16" height="16" viewBox="0 0 16 16"><path d="M3 5h10l-1 9H4z" fill="none" stroke="#d3a22b" stroke-width="1.4"/><path d="M6 5V3.5a2 2 0 0 1 4 0V5" fill="none" stroke="#d3a22b" stroke-width="1.4"/></svg><span class="count">0</span></div>
    </header>
    <nav class="nav">
      <span class="active">HOME</span><span>NEW ARRIVALS</span><span>PRE ORDER</span><span>MEN COLLECTION</span><span>WOMEN COLLECTION ▾</span><span>SEASON COLLECTIONS ▾</span><span>BAGS</span><span>ACCESSORIES</span>
    </nav>
    <section class="banner">
      <h1>HIGH HEELS</h1>
      <div class="photo" role="img" aria-label="Row of women's high heel shoes in tan and black"></div>
      <div class="crumbs"><b>Home</b> / Women Collection / High Heels</div>
    </section>
    <section class="product">
      <div class="gallery"><div class="shoe" role="img" aria-label="Blue lace-up high heel shoe"></div></div>
      <div class="info">
        <h2>Blue High Heels</h2>
        <dl class="specs">
          <dt>EFFECTIVE PRICE</dt><dd>R 00.00</dd>
          <dt>BRAND</dt><dd>Morvetta</dd>
          <dt>MATERIAL</dt><dd>Genuine Leather</dd>
          <dt>AVAILABILITY</dt><dd>Ready In Stock</dd>
        </dl>
        <div class="rule"></div>
        <div class="opts">
          <span>COLOR</span><div class="swatches"><i style="background:#4a5566"></i><i style="background:#c8b08a"></i><i style="background:#b9b9b9"></i><i style="background:#2a2a2a"></i></div>
          <span>SIZE</span><div class="sel">6 ▾</div>
          <span>QUANTITY</span><div class="sel">1 ▾</div>
          <span>SUBTOTAL</span><div>R 00.00</div>
        </div>
        <div class="buttons"><span class="btn">ADD TO CART</span><span class="btn">BUY IT NOW</span><span class="btn">ADD WISHLIST</span></div>
      </div>
    </section>
    <p class="summary">Crafted from soft imported leather, this blue heel pairs a lace-up front with a slim stiletto and cushioned insole. Smart enough for the office, elegant enough for evening plans and comfortable all day long.</p>
    <div class="tabs"><div class="on">Description</div><div>Reviews</div><div>Shipping Details</div></div>
    <p class="tabtext">Our blue high heel is made by hand from genuine imported leather with a fine suede finish. The pointed toe and laced vamp give a classic shape, while the padded footbed keeps each step light. A leather lining lets the foot breathe and the rubber tip on the heel adds grip on smooth floors. Wipe clean with a soft dry cloth and store in the dust bag supplied. Sizes run true, so choose your usual size. Delivery is offered across South Africa and neighbouring countries with tracking on every order.</p>
  </div>
  <footer class="footer">
    <div class="footcard">
      <div>
        <h3>INFORMATION</h3>
        <ul class="links"><li>About Us</li><li>Terms &amp; Conditions</li><li>Privacy Policy</li><li>Returns &amp; Exchanges</li><li>Payments</li><li>Contact Us</li></ul>
      </div>
      <div class="newsletter">
        <h3>NEWSLETTER</h3>
        <p>Subscribe to get first news on new arrivals, sale alerts and a discount code for your next order.</p>
        <div class="signup">Enter your email <b><svg width="8" height="8" viewBox="0 0 10 10"><path d="M1 5l8-4-3 8-1-3z" fill="#fff"/></svg></b></div>
      </div>
      <div class="contact">
        <h3>CONTACT US</h3>
        <p>12 Kestrel Lane, Rosewood<br>Johannesburg 2000, South Africa<br>Tel: 080 555 01 234<br>Fax: 080 555 01 235<br>hello@morvetta.shop</p>
      </div>
    </div>
  </footer>
  <div class="bottombar">
    <div class="pay">Pay Via <strong>QuidLane</strong><span class="chip"></span><strong>Vantra</strong><span class="chip"></span><strong>Meridcard</strong></div>
    <div class="powered">Powered by <b>Morvetta</b> © 2020</div>
    <div class="findus">Find Us At <span class="dot"></span><span class="dot"></span><span class="dot"></span></div>
  </div>
</div>
</body>
</html>
```